Swimming Pool Business Billboard

10' x 24' Billboard displaying company name, logo and phone number. Picture of swimming pool activity; kids playing , swimming, etc. Bullet points possibly shown: New Construction, Repairs, Weekly maintenance.

Industry/Entity Type

Swimming pool construction, repairs and maintenance.

Font styles to use
Sans Serif

Colors
0054AA
0677BA
7BADD7
CADEEF
E8F1F8

Requirements
Must have
• Rusty & Calder Pembrook, RUSTY'S POOLS & Service,
Nice to have
• Prefer to have my last name "Pembrook" above the word "POOLS" only in smaller print so that "RUSTYS POOLS" is distinguished.

```html
<!DOCTYPE html>
<html lang="en">
<head>
<meta charset="utf-8">
<title>Rusty's Pools and Service Billboard</title>
<link href="https://fonts.googleapis.com/css2?family=Poppins:wght@600;700;800&display=swap" rel="stylesheet">
<style>
  :root {
    --canvas: #ffffff;
    --teal: #67bcc8;
    --navy: #172a52;
    --bullet: #1a8fe0;
    --white: #ffffff;
    --water-deep: #1fa3c4;
    --water-light: #7fd7e6;
    --facade: #5b6a72;
  }
  * { margin: 0; padding: 0; box-sizing: border-box; }
  html, body { width: 1200px; height: 1200px; overflow: hidden; background: var(--canvas); }
  body { position: relative; font-family: "Poppins", sans-serif; color: var(--navy); }

  .billboard {
    position: absolute; left: 83px; top: 385px;
    width: 1033px; height: 430px;
    background: var(--teal); overflow: hidden;
  }
  .photo-art { position: absolute; left: 0; top: 0; }

  .owners {
    position: absolute; right: 20px; top: 16px;
    font-size: 27px; font-weight: 700; letter-spacing: 3.4px; white-space: nowrap;
  }
  .headline {
    position: absolute; left: 392px; top: 48px; width: 622px;
    text-align: center; font-weight: 800; line-height: 88px; font-size: 66px;
    letter-spacing: 0.5px;
  }
  .headline .line-two { display: block; padding-right: 40px; }

  .services {
    position: absolute; left: 420px; top: 237px; width: 613px; height: 100px;
    background: var(--navy); color: var(--white);
    font-size: 27px; font-weight: 700; text-align: center; padding-top: 6px; line-height: 43px;
  }
  .services .row { display: block; white-space: nowrap; }
  .services .item { margin: 0 6px; }
  .services .item::before {
    content: ""; display: inline-block; width: 20px; height: 20px; border-radius: 50%;
    background: var(--bullet); margin-right: 16px; vertical-align: 1px;
  }

  .website {
    position: absolute; right: 14px; top: 340px;
    font-size: 22px; font-weight: 700; letter-spacing: 2.4px; white-space: nowrap;
  }
  .contact {
    position: absolute; right: 12px; top: 373px;
    font-size: 32px; font-weight: 800; letter-spacing: 0.6px; white-space: nowrap;
    display: flex; align-items: center; gap: 34px;
  }
  .contact .phone { display: flex; align-items: center; gap: 6px; }

  .brand-mark {
    position: absolute; left: 290px; top: 320px; width: 120px;
    text-align: center; font-size: 16px; font-weight: 800; line-height: 18px; color: var(--navy);
  }
  .brand-mark::before {
    content: ""; display: block; width: 34px; height: 34px; border-radius: 50%;
    background: var(--navy); margin: 0 auto 6px;
  }
</style>
</head>
<body>
  <section class="billboard">
    <svg class="photo-art" width="1033" height="430" viewBox="0 0 1033 430">
      <defs>
        <linearGradient id="poolScene" x1="0" y1="0" x2="0" y2="1">
          <stop offset="0" stop-color="#6f7c82"/>
          <stop offset="0.55" stop-color="#4c6a70"/>
          <stop offset="0.62" stop-color="#5fc7da"/>
          <stop offset="1" stop-color="#1fa3c4"/>
        </linearGradient>
      </defs>
      <path class="curve-edge" d="M322 0 C355 120 440 215 432 320 C426 385 400 412 365 430 H0 V0 Z" fill="var(--navy)"/>
      <path class="curve-band" d="M328 0 C360 118 432 215 424 318 C418 380 392 410 358 430 H0 V0 Z" fill="var(--white)"/>
      <path d="M328 0 C350 110 400 200 392 300 C386 370 360 408 330 430 H0 V0 Z"
            fill="url(#poolScene)" role="img"
            aria-label="Photo of two children in swim gear jumping from the edge into a bright blue pool"/>
    </svg>

    <div class="brand-mark">RUSTYS POOLS</div>

    <div class="owners">RUSTY &amp; CALDER PEMBROOK</div>
    <h1 class="headline">RUSTY'S POOLS<span class="line-two">AND SERVICE</span></h1>

    <div class="services">
      <span class="row"><span class="item">NEW CONSTRUCTION</span><span class="item">REPAIRS</span></span>
      <span class="row"><span class="item">WEEKLY MAINTENANCE</span></span>
    </div>

    <div class="website">www.rustycalderpembrook.com</div>
    <div class="contact">
      <span class="address">ADD: XXXXXXXXX</span>
      <span class="phone">
        <svg width="16" height="26" viewBox="0 0 16 26" aria-hidden="true">
          <path d="M12 2 C6 2 3 7 3 13 C3 19 6 24 12 24 L13 19 L9 18 C8 15 8 11 9 8 L13 7 Z" fill="var(--navy)"/>
        </svg>: 945380126
      </span>
    </div>
  </section>
</body>
</html>
```